Tarjetas de visita para empresa de aluminio

Empresa con mas de 40 años vendiendo perfiles de aluminio.
Somos fábrica y almacén, queremos renovar la tarjeta de presentación de nuestros comerciales dando una imgen innovadora y tecnógica mezclado con la calidez del respeto al medio ambiente.
Añado el logo de la empresa y actual cara trasera de la tarjeta de visita, el logo es el simbolo WM y la marca TRAVENIC EXTRUSION, la frase 2extrusion y lacado de aluminio" debe cambiarse por "Diseño, extrusión, lacado, anodizado y mecanizado de precisión de aluminio" o en su defecto incluir todos esos servicios que hacemos o una frase mas pegadiza.

We are an aluminium factory, we produce and stock profiles of aluminium.
we want to renew visit card of our sellers, we are looking for something that show innovation, tecnology and environment respect.
Upload our actual logo and back of visit card, logo WM and brand TRAVENIC EXTRUSION must be keept.
Text "Extrusion y lacado de aluminio" must be changed for "Diseño, extrusion, lacado, anodizado y mecanizado de precisión de aluminio" or something like that

```html
<!DOCTYPE html>
<html lang="es">
<head>
<meta charset="utf-8">
<title>Travenic Extrusion – Tarjetas de visita</title>
<link rel="stylesheet" href="https://fonts.googleapis.com/css2?family=Michroma&family=Montserrat:wght@400;500;700&display=swap">
<style>
  :root {
    --bg: #2b2c2e;
    --blue-deep: #08486b;
    --blue-mid: #1f5c86;
    --blue-soft: #3a7595;
    --silver-light: #f4f6f8;
    --silver: #c9ced3;
    --silver-dark: #8e959c;
    --ink-black: #0e0f10;
    --text-light: #eef1f4;
    --name-blue: #1d4f7e;
  }
  * { box-sizing: border-box; margin: 0; padding: 0; }
  html, body { width: 1200px; height: 1186px; overflow: hidden; }
  body {
    background: var(--bg);
    font-family: "Montserrat", sans-serif;
    position: relative;
  }
  .card {
    position: absolute;
    left: 198px;
    width: 804px;
    height: 520px;
    border-radius: 34px;
    overflow: hidden;
  }
  .card--front {
    top: 40px;
    background: linear-gradient(210deg, var(--blue-deep) 0%, var(--blue-mid) 50%, var(--blue-soft) 100%);
  }
  .card--back { top: 606px; background: var(--ink-black); }

  .brand {
    display: flex;
    align-items: center;
    justify-content: center;
    gap: 18px;
  }
  .brand__dot {
    border-radius: 50%;
    background: var(--silver);
    flex: none;
  }
  .brand__name {
    font-family: "Michroma", sans-serif;
    color: var(--silver);
    white-space: nowrap;
  }

  .front__brand { position: absolute; top: 180px; left: 40px; right: 40px; }
  .front__brand .brand__dot { width: 46px; height: 46px; }
  .front__brand .brand__name { font-size: 33px; letter-spacing: 1px; }
  .front__tagline {
    position: absolute;
    top: 268px; left: 40px; right: 40px;
    text-align: center;
    font-family: "Michroma", sans-serif;
    color: var(--silver);
    font-size: 18px;
    line-height: 1.7;
    letter-spacing: 0.5px;
  }

  .back__top {
    position: absolute; top: 0; left: 0; right: 0; height: 290px;
    background: linear-gradient(200deg, var(--blue-mid) 0%, var(--blue-deep) 100%);
  }
  .back__brand { position: absolute; top: 110px; left: 40px; right: 40px; }
  .back__brand .brand__dot { width: 34px; height: 34px; }
  .back__brand .brand__name { font-size: 28px; letter-spacing: 1px; }
  .back__tagline {
    position: absolute; top: 168px; left: 40px; right: 40px;
    text-align: center;
    color: var(--text-light);
    font-size: 12px;
    font-weight: 500;
  }
  .back__band {
    position: absolute; top: 290px; left: 0; right: 0; height: 76px;
    background: linear-gradient(180deg, var(--silver-dark) 0%, var(--silver-light) 35%, var(--silver) 70%, var(--silver-dark) 100%);
  }
  .person { position: absolute; top: 298px; left: 0; right: 0; text-align: center; }
  .person__name {
    color: var(--name-blue);
    font-weight: 700;
    font-size: 27px;
    letter-spacing: 1px;
    line-height: 1.2;
  }
  .person__role { color: var(--name-blue); font-size: 18px; margin-top: 2px; }

  .contacts {
    position: absolute; left: 50px; top: 388px;
    list-style: none;
    color: var(--text-light);
    font-size: 18px;
  }
  .contacts li { display: flex; align-items: center; gap: 16px; height: 23px; }
  .contacts svg { width: 17px; height: 17px; fill: var(--text-light); flex: none; }
  .address {
    position: absolute; right: 48px; top: 388px;
    text-align: right;
    color: var(--text-light);
    font-size: 18px;
    line-height: 1.3;
    font-style: normal;
  }
</style>
</head>
<body>

<section class="card card--front" aria-label="Cara frontal">
  <div class="brand front__brand">
    <span class="brand__dot"></span>
    <span class="brand__name">TRAVENIC EXTRUSION</span>
  </div>
  <p class="front__tagline">DISEÑO · EXTRUSION · LACADO · ANODIZADO<br>Y MECANIZADO DE PRECISIÓN DE ALUMINIO</p>
</section>

<section class="card card--back" aria-label="Cara trasera">
  <div class="back__top"></div>
  <div class="brand back__brand">
    <span class="brand__dot"></span>
    <span class="brand__name">TRAVENIC EXTRUSION</span>
  </div>
  <p class="back__tagline">Diseño, extrusion, lacado, anodizado y mecanizado de precisión de aluminio</p>
  <div class="back__band"></div>
  <div class="person">
    <p class="person__name">MARCOS FERRER LOZANO</p>
    <p class="person__role">Comercial</p>
  </div>

  <ul class="contacts">
    <li><svg viewBox="0 0 24 24"><path d="M6.6 10.8a15 15 0 0 0 6.6 6.6l2.2-2.2a1 1 0 0 1 1-.25 11.4 11.4 0 0 0 3.6.6 1 1 0 0 1 1 1V20a1 1 0 0 1-1 1A17 17 0 0 1 3 4a1 1 0 0 1 1-1h3.5a1 1 0 0 1 1 1c0 1.25.2 2.45.6 3.6a1 1 0 0 1-.25 1z"/></svg>950 41 22 17</li>
    <li><svg viewBox="0 0 24 24"><path d="M7 1h10a2 2 0 0 1 2 2v18a2 2 0 0 1-2 2H7a2 2 0 0 1-2-2V3a2 2 0 0 1 2-2zm0 3v14h10V4z"/></svg>611 58 34 92</li>
    <li><svg viewBox="0 0 24 24"><path d="M6 2h9l3 3v4h2a2 2 0 0 1 2 2v9a2 2 0 0 1-2 2H4a2 2 0 0 1-2-2v-9a2 2 0 0 1 2-2h2zm2 2v5h8V6h-2V4zM5 13v2h3v-2zm5 0v2h3v-2zm5 0v2h3v-2zM5 17v2h3v-2zm5 0v2h3v-2zm5 0v2h3v-2z"/></svg>950 41 22 80</li>
    <li><svg viewBox="0 0 24 24"><path d="M2 5h20v14H2zm2 2v.5l8 5 8-5V7zm0 3v7h16v-7l-8 5z"/></svg>marcosferrer@travenic.com</li>
    <li><svg viewBox="0 0 24 24"><path d="M12 2a10 10 0 1 0 0 20 10 10 0 0 0 0-20zm6.9 9h-3a15 15 0 0 0-1.3-5.5A8 8 0 0 1 18.9 11zM12 4c.9 1.2 1.8 3.6 2 7h-4c.2-3.4 1.1-5.8 2-7zM9.4 5.5A15 15 0 0 0 8.1 11h-3a8 8 0 0 1 4.3-5.5zM5.1 13h3a15 15 0 0 0 1.3 5.5A8 8 0 0 1 5.1 13zm6.9 7c-.9-1.2-1.8-3.6-2-7h4c-.2 3.4-1.1 5.8-2 7zm2.6-1.5a15 15 0 0 0 1.3-5.5h3a8 8 0 0 1-4.3 5.5z"/></svg>www.travenic.com</li>
  </ul>

  <address class="address">
    Pol. Ind. El Prado, C/ 4 nº 12<br>
    14900 Lucena – Córdoba<br>
    Apartado de correos 305
  </address>
</section>

</body>
</html>
```